Zielgruppe
Unsere Firma produziert individuelles Büromaterialen aus Papier & Kunststoff (bspw. Ringbücher, Klarsichthüllen, Mappen, etc.) Zielgruppe sind (eher konservative) Unternehmenskunden in allen Branchen (speziell Logistik, KFZ, Gesundheit).
Die Broschüre soll primär zur Neukundenakquise als auch für Neuverkäufe an Bestandskunden verwendet werden und in einem schlichten, modernen und hochwertigen Design eine Übersicht über unser Produktportfolio bieten.
Aufgabenstellung
Die Broschüre soll auf Basis des bestehenden Corporate Designs gestaltet werden.
1) In der Broschüre soll jede unserer fünf Produktkategorien (Ordner, Ringbuchordner, Ordnerregister, Hüllen & Taschen, Mappen) eine eigene Seite/Abschnitt erhalten, ähnlich unserer Website.
2) Zudem soll auf einer eigenen Seite/Abschnitt prägnant darauf hingewiesen werden, dass wir für alle Produktkategorie individuelle Sonderanfertigungen anbieten.
Die Strukturierung und Aufteilung der Inhalt in der Broschüre soll sich relativ klar an unserer Website orientieren. Medien & bereits vorhandene Texte sind sowohl als Anlage dem Projekt beigefügt, als auch auf unserer Website auffindbar. Falls notwendig wären wir auch bereit zu einzelnen Themenbereiche neue Texte erstellen zu lassen.
Hinsichtlich des Formats überlassen wir die Auswahl dem Designer. Die Broschüre wird jedoch auch häufig in digitaler Form versandt.

```html
<!DOCTYPE html>
<html lang="de">
<head>
<meta charset="utf-8">
<title>Holtmann Bürotechnik – Produktübersicht 2022</title>
<link rel="stylesheet" href="https://fonts.googleapis.com/css2?family=Saira:wght@400;500&display=swap">
<style>
  :root {
    --brand-blue: #1a3c86;
    --ink: #2a2f3a;
    --paper: #f7f8fa;
    --band: #d3d9e6;
    --veil: rgba(225, 232, 242, 0.72);
    --veil-accent: rgba(160, 172, 214, 0.8);
    --backdrop: #a6adb5;
  }
  * { box-sizing: border-box; margin: 0; padding: 0; }
  html, body {
    width: 1200px; height: 960px; overflow: hidden;
    background: var(--backdrop);
    font-family: "Saira", sans-serif;
  }
  .spread {
    position: absolute; left: 180px; top: 183px;
    width: 840px; height: 594px;
    display: flex;
    box-shadow: 0 10px 30px rgba(0,0,0,0.18);
  }
  .page {
    position: relative; width: 420px; height: 594px;
    background: var(--paper); overflow: hidden;
  }
  .page svg.shapes { position: absolute; inset: 0; }

  .brand-name {
    color: var(--ink); font-size: 14px; font-weight: 400;
    letter-spacing: 0.3px; line-height: 18px; white-space: nowrap;
  }

  /* Back cover */
  .back-brand { position: absolute; left: 40px; top: 440px; }
  .contact {
    position: absolute; left: 40px; top: 476px;
    font-style: normal;
    font-size: 9px; line-height: 12px; color: var(--ink); letter-spacing: 0.2px;
  }
  .contact .company { color: var(--brand-blue); font-size: 9.5px; line-height: 12px; margin-bottom: 2px; }

  /* Front cover */
  .front-brand { position: absolute; right: 34px; top: 36px; text-align: right; }
  .cover-title {
    position: absolute; left: 50px; top: 374px;
    color: var(--brand-blue); font-size: 21px; line-height: 28px;
    letter-spacing: 0.4px; font-weight: 500;
  }
  .cover-title .line-two { display: block; padding-left: 16px; }
  .cover-subtitle {
    position: absolute; left: 66px; top: 442px;
    color: var(--ink); font-size: 10.5px; letter-spacing: 1px;
  }
</style>
</head>
<body>
<main class="spread">

  <section class="page back-cover" aria-label="Rückseite">
    <svg class="shapes" width="420" height="594" viewBox="0 0 420 594">
      <path class="contact-band" d="M0,405 C150,400 300,365 420,305 L420,562 L0,562 Z" fill="var(--band)"/>
    </svg>
    <div class="back-brand">
      <div class="brand-name">Holtmann Bürotechnik</div>
    </div>
    <address class="contact">
      <div class="company">Holtmann UG Papier-<br>&amp; Kunststoffverarbeitung</div>
      Lindenweg 12<br>
      45127 Musterstadt<br>
      Telefon: +49 201 5550 12<br>
      E-Mail: kontakt@holtmann-buero.de
    </address>
  </section>

  <section class="page front-cover" aria-label="Titelseite">
    <svg class="shapes" width="420" height="594" viewBox="0 0 420 594">
      <defs>
        <linearGradient id="photoTone" x1="0" y1="0" x2="1" y2="1">
          <stop offset="0" stop-color="#dfe5ee"/>
          <stop offset="0.45" stop-color="#b9cfe0"/>
          <stop offset="0.75" stop-color="#c8d6e4"/>
          <stop offset="0.88" stop-color="#d9a57a"/>
          <stop offset="1" stop-color="#e9edf2"/>
        </linearGradient>
      </defs>
      <g role="img" aria-label="Foto: geöffnete Ringbuchmechanik mit Metallringen und eingehefteten Papierblättern">
        <path class="cover-photo" d="M0,130 C140,128 290,110 420,78 L420,515 L0,515 Z" fill="url(#photoTone)"/>
      </g>
      <rect class="accent-bar" x="374" y="104" width="17" height="243" fill="var(--brand-blue)"/>
      <rect class="title-veil" x="0" y="347" width="374" height="133" fill="var(--veil)"/>
      <rect class="title-veil-accent" x="374" y="347" width="46" height="83" fill="var(--veil-accent)"/>
      <rect class="accent-block" x="391" y="430" width="29" height="50" fill="var(--brand-blue)"/>
    </svg>
    <div class="front-brand">
      <div class="brand-name">Holtmann Bürotechnik</div>
    </div>
    <h1 class="cover-title">Papier und Kunststoff<span class="line-two">sind unser Ding!</span></h1>
    <p class="cover-subtitle">PRODUKTÜBERSICHT 2022</p>
  </section>

</main>
</body>
</html>
```